Need help refining Solkvartsgillet

Hi We need help with the refining of overall design and details of our homepage design Solkvartsgillet. See attached files.

Attached files:
homepage.psd - file you can use to work from.
homepage.png – quick notes on thoughts of the design
logo.psd (smart object) – The logo should be in gold.
social media elements.png - what type of data that needs design in the feed

What we need:
Something is missing with the overall design as well as detailed design for our social media feed. We don’t know what and hope you can solve this for us.

The homepage:
Our main page include a selfloading blogfeed combined with Pageloop- and Instagramfeed.

Fonts:
So far I´ve used Roboto regular, and Georgia, but feel free to use other fonts if you find better suited

Among others, we need a better detailed design that works better with the overall design.

Se attached sample image (social_mediafeed.png) what types of data we get from Pageloop in our feed. Feel free to redesign the elements of this data.

Headerlinks:
Even though we only have one page, there should be place for links to other pages as well which will load below the header.

Social media follow: Place for social media follow links/icons/buttons in style with rest of the design. Maybe at top grey border? We use Glimtora and Pageloop in style with rest of the design.

Colors:
The logo should be in gold, and use of "goldish" colors troughout the page.
Also blue elements troughout the page

Logo in gold/goldish color
Blue elements # 13416c (or similar color that works well in the design)

Target Market(s)

Wellness, fitness, spa and food, Exclusive

Number of Pages Required

1 page

Font styles to use
Serif
Sans Serif
Script
Other font styles liked:
• Roboto, Georgia

Requirements
Must have
• Better overall design that feel harmonic.
• Better design of blog and social media feeds (se all attached images)
• Nice clean design, easy on the eye
• Colors on theme: Gold + blue

```html
<!DOCTYPE html>
<html lang="en">
<head>
<meta charset="utf-8">
<title>Solkvartsgillet — Home</title>
<link href="https://fonts.googleapis.com/css2?family=Montserrat:wght@400;500;600;700&family=Libre+Baskerville:ital@0;1&display=swap" rel="stylesheet">
<style>
:root{
  --blue:#13416c;
  --blue-dark:#0f3558;
  --gold:#f3c144;
  --gold-tag:#f0b73a;
  --gold-foot:#d4982b;
  --gold-text:#e8b23c;
  --page:#f3f3f3;
  --card:#ffffff;
  --ink:#2b2b2b;
  --muted:#777777;
  --line:#e6e6e6;
  --dark:#262626;
  --topbar:#f6f6f6;
}
*{box-sizing:border-box;margin:0;padding:0}
html,body{width:1200px;height:3249px;overflow:hidden}
body{position:relative;background:var(--blue);font-family:'Montserrat',Arial,sans-serif;color:var(--ink)}
.abs{position:absolute}

/* top bar */
.topbar{top:0;left:0;width:1200px;height:35px;background:var(--topbar);display:flex;align-items:center}
.topbar .follow{position:absolute;left:326px;display:flex;gap:14px}
.topbar .follow span{width:7px;height:7px;border-radius:50%;background:#9aa3ad}
.topbar .account{position:absolute;left:772px;font-size:9px;letter-spacing:1px;color:#8a8a8a;display:flex;align-items:center;gap:6px}
.topbar .account svg{width:9px;height:9px}

/* header */
.header{top:35px;left:0;width:1200px;height:91px;background:var(--blue)}
.nav{position:absolute;top:35px;display:flex;gap:0;font-size:10px;font-weight:600;letter-spacing:1px;color:#fff;text-transform:uppercase}
.nav a{color:#fff;text-decoration:none;margin-right:52px}
.nav a.active{color:var(--gold)}
.nav.left{left:266px}
.nav.right{left:700px}
.nav.left::after,.nav.right::after{content:"";position:absolute;left:0;right:52px;top:20px;height:1px;background:rgba(255,255,255,.35)}
.brand{left:530px;top:8px;width:140px;text-align:center}
.brand .mark{width:34px;height:34px;margin:0 auto 6px;border-radius:50%;background:var(--gold)}
.brand .name{font-size:13px;font-weight:700;letter-spacing:1px;color:var(--gold);text-transform:uppercase;border:0}

/* hero */
.hero{top:126px;left:0;width:1200px;height:329px;overflow:hidden}
.hero .side{position:absolute;top:0;width:210px;height:329px;background:linear-gradient(180deg,#c9d4e2 0%,#e9e4ea 55%,#b9c6d6 100%);opacity:.85}
.hero .side.l{left:0}
.hero .side.r{left:990px}
.hero .side .arrow{position:absolute;top:130px;width:22px;height:72px;border:1px solid #fff;background:rgba(19,65,108,.55);display:flex;align-items:center;justify-content:center}
.hero .side.l .arrow{left:87px}
.hero .side.r .arrow{left:100px}
.hero .main{position:absolute;left:210px;top:0;width:780px;height:329px;background:linear-gradient(180deg,#3a4d66 0%,#b7a79a 45%,#8b8f98 70%,#5d5a58 100%)}
.hero .caption{position:absolute;left:210px;width:780px;top:86px;text-align:center;color:#fff}
.tag{display:inline-block;background:var(--gold-tag);color:#fff;font-size:8px;font-weight:600;letter-spacing:1px;padding:4px 10px;text-transform:uppercase}
.hero h1{font-size:19px;font-weight:500;margin-top:12px;letter-spacing:.3px}
.hero .byline{font-family:'Libre Baskerville',Georgia,serif;font-style:italic;font-size:10px;margin-top:8px}
.btn-outline{display:inline-block;border:1px solid #fff;color:#fff;font-size:8px;font-weight:600;letter-spacing:1px;padding:8px 18px;text-transform:uppercase;margin-top:18px}
.hero .dots{position:absolute;left:0;width:780px;top:280px;display:flex;justify-content:center;gap:5px}
.hero .dots span{width:5px;height:5px;border-radius:50%;background:rgba(255,255,255,.7)}
.hero .dots span:first-child{background:#fff;width:6px;height:6px}

/* content column */
.column{top:455px;left:210px;width:780px;height:2426px;background:var(--page)}
.section-title{position:absolute;left:0;width:780px;text-align:center;font-size:20px;font-weight:600;color:#222}
.offers-title{top:26px}
.offers{position:absolute;top:71px;left:39px;width:702px;height:330px;background:var(--gold)}
.offer{position:absolute;top:15px;width:210px;height:271px;overflow:hidden}
.offer .photo{position:absolute;inset:0}
.offer .panel{position:absolute;left:21px;right:21px;top:135px;height:126px;background:rgba(30,30,30,.55);text-align:center;color:#fff}
.offer .panel .tag{position:relative;top:-8px}
.offer .pct{font-size:17px;font-weight:600;margin-top:0}
.offer .desc{font-size:10px;line-height:14px;margin-top:3px}
.offer .btn-outline{margin-top:10px;padding:6px 14px;font-size:7px}
.offers .arrows{position:absolute;left:16px;top:304px;display:flex;gap:8px}
.divider{position:absolute;top:433px;left:0;width:780px;height:1px;background:#e2e2e2}
.blog-title{top:470px}

/* cards */
.card{position:absolute;background:var(--card);box-shadow:0 1px 3px rgba(0,0,0,.07);text-align:center}
.card .img{position:relative}
.card .img .tag{position:absolute;left:50%;bottom:-8px;transform:translateX(-50%)}
.card .date{font-family:'Libre Baskerville',Georgia,serif;font-size:8px;color:#333;margin-top:22px}
.card h3{font-size:11.5px;font-weight:500;line-height:15px;color:#222;margin-top:8px}
.card p{font-family:'Libre Baskerville',Georgia,serif;font-size:8.5px;line-height:13px;color:#777;margin:10px auto 0}
.card .meta{display:flex;justify-content:space-between;align-items:center;font-family:'Libre Baskerville',Georgia,serif;font-size:8px;color:var(--blue);border-top:1px solid var(--line);border-bottom:1px solid var(--line);padding:9px 0;margin:0 auto}
.card .meta span{display:flex;align-items:center;gap:4px}
.card .meta svg{width:9px;height:9px}
.card .more{font-family:'Libre Baskerville',Georgia,serif;font-size:8.5px;color:var(--gold-text)}

.card.big{width:340px;height:505px;top:513px;padding:16px 16px 0}
.card.big .img{height:239px}
.card.big .ribbon{position:absolute;left:-16px;top:0;width:16px;height:70px;background:var(--blue);color:#fff;font-size:7px;font-family:'Libre Baskerville',Georgia,serif;writing-mode:vertical-rl;transform:rotate(180deg);display:flex;align-items:center;justify-content:center}
.card.big h3{margin-top:26px}
.card.big p{width:290px}
.card.big .meta{width:308px;margin-top:22px;position:absolute;left:16px;top:402px}
.card.big .more{position:absolute;left:0;width:340px;top:452px}

.card.small{width:221px;height:416px;padding:14px 14px 0}
.card.small .img{height:122px}
.card.small h3{width:150px;margin-left:auto;margin-right:auto}
.card.small p{width:176px}
.card.small .meta{position:absolute;left:14px;width:193px;top:318px}
.card.small .more{position:absolute;left:0;width:221px;top:370px}

.widget{position:absolute;width:221px;background:var(--card);box-shadow:0 1px 3px rgba(0,0,0,.07)}
.widget .head{background:var(--blue);color:#fff;font-size:11px;font-weight:500;text-align:center;height:35px;line-height:35px}

.pl-feed{height:345px;margin:12px 18px;border:1px solid #dcdcdc;position:relative;overflow:hidden}
.pl-cover{height:78px;background:linear-gradient(135deg,#6b5140,#a8927c);position:relative}
.pl-cover .nm{position:absolute;left:40px;top:6px;color:#fff;font-size:9px;font-weight:600}
.pl-cover .lk{position:absolute;left:40px;top:19px;color:#fff;font-size:6.5px}
.pl-cover .av{position:absolute;left:6px;top:6px;width:28px;height:28px;background:#3a2f28;border:1px solid #fff}
.pl-cover .bt{position:absolute;top:56px;height:13px;background:#f2f2f2;border:1px solid #ccc;font-size:6px;line-height:11px;padding:0 5px;color:#333}
.pl-feed .line{font-size:6.5px;color:#555;padding:4px 6px;border-bottom:1px solid #eee}
.pl-post{padding:6px}
.pl-post .who{display:flex;gap:5px;align-items:center;font-size:6.5px;color:var(--blue);font-weight:600}
.pl-post .who i{width:18px;height:18px;background:#3a2f28;display:block}
.pl-post .txt{font-size:6.5px;color:#333;line-height:9px;margin-top:5px}
.pl-post .pic{height:150px;margin-top:6px;background:linear-gradient(180deg,#7ea7d8,#c9d9ee 60%,#3b3b3b)}

.ig-handle{font-family:'Libre Baskerville',Georgia,serif;font-size:8px;color:#666;padding:14px 18px 0}
.ig-stats{display:flex;margin:10px 18px 0;border-top:1px solid var(--line);border-bottom:1px solid var(--line);font-size:7.5px;color:#666}
.ig-stats span{flex:1;display:flex;align-items:center;justify-content:center;gap:4px;padding:7px 0}
.ig-stats span+span{border-left:1px solid var(--line)}
.ig-stats i{width:8px;height:8px;background:var(--gold-tag);display:block}
.ig-grid{display:grid;grid-template-columns:repeat(3,46px);gap:13px 18px;justify-content:center;margin-top:18px}
.ig-grid div{height:46px}
.ig-foot{font-family:'Libre Baskerville',Georgia,serif;font-size:7px;color:#666;text-align:right;padding:16px 18px 0}

.load-more{position:absolute;top:2361px;left:343px;width:94px;height:26px;border:1px solid var(--blue);color:var(--blue);font-size:8px;font-weight:600;letter-spacing:1px;text-align:center;line-height:24px;background:#fff}

/* footers */
.foot-gold{top:2881px;left:0;width:1200px;height:212px;background:var(--gold-foot);text-align:center;color:#fff}
.foot-gold .mark{width:22px;height:22px;border-radius:50%;background:#fff;margin:34px auto 5px}
.foot-gold .name{font-size:10px;font-weight:700;letter-spacing:1px;text-transform:uppercase}
.foot-gold p{font-family:'Libre Baskerville',Georgia,serif;font-size:9px;line-height:13px;width:300px;margin:10px auto 0;font-weight:bold}
.foot-gold .sub{font-size:11px;margin-top:28px}
.foot-gold form{display:flex;justify-content:center;margin-top:10px}
.foot-gold .input{width:255px;height:21px;background:#fff;font-family:'Libre Baskerville',Georgia,serif;font-size:8px;color:#999;text-align:left;padding-left:8px;line-height:21px}
.foot-gold .send{width:21px;height:21px;background:var(--blue);display:flex;align-items:center;justify-content:center}
.foot-dark{top:3093px;left:0;width:1200px;height:156px;background:var(--dark);text-align:center}
.foot-dark .icons{display:flex;justify-content:center;gap:10px;margin-top:30px}
.foot-dark .icons span{width:21px;height:21px;border-radius:50%;border:1px solid #777}
.foot-dark .icons span.on{background:var(--gold-foot);border-color:var(--gold-foot)}
.foot-dark .copy{font-family:'Libre Baskerville',Georgia,serif;font-size:8.5px;color:#bbb;margin-top:46px}
</style>
</head>
<body>

<div class="abs topbar">
  <div class="follow"><span></span><span></span><span></span><span></span><span></span></div>
  <div class="account">
    <svg viewBox="0 0 10 10"><circle cx="5" cy="3" r="2.2" fill="#9a9a9a"/><path d="M1 10c0-3 2-4.5 4-4.5S9 7 9 10z" fill="#9a9a9a"/></svg>
    LOGIN &nbsp;/&nbsp; SIGN UP
  </div>
</div>

<header class="abs header">
  <nav class="nav left"><a href="#">Home</a><a class="active" href="#">About Us</a><a href="#">Inspiration</a></nav>
  <div class="abs brand"><div class="mark"></div><div class="name">Solkvartsgillet</div></div>
  <nav class="nav right"><a href="#">Member Offers</a><a href="#">On</a><a href="#">Contact Us</a></nav>
</header>

<section class="abs hero">
  <div class="side l" role="img" aria-label="Overwater villas at dusk, faded">
    <div class="arrow"><svg width="8" height="10" viewBox="0 0 8 10"><path d="M6 1L2 5l4 4" stroke="#fff" fill="none" stroke-width="1.4"/></svg></div>
  </div>
  <div class="main" role="img" aria-label="Photographer on a rocky ridge above the sea at sunset"></div>
  <div class="side r" role="img" aria-label="Overwater villas in pale morning light, faded">
    <div class="arrow"><svg width="8" height="10" viewBox="0 0 8 10"><path d="M2 1l4 4-4 4" stroke="#fff" fill="none" stroke-width="1.4"/></svg></div>
  </div>
  <div class="caption">
    <span class="tag">Life Style</span>
    <h1>How to Spend a Week in the Maldives</h1>
    <div class="byline">June 28th, 2016 &nbsp;–&nbsp; By Elin Varg</div>
    <span class="btn-outline">Read More</span>
  </div>
  <div class="abs dots" style="left:210px"><span></span><span></span><span></span><span></span></div>
</section>

<main class="abs column">
  <h2 class="section-title offers-title">Member Offers</h2>
  <div class="offers">
    <article class="offer" style="left:16px">
      <div class="photo" role="img" aria-label="Mountain valley seen from a plane window" style="background:linear-gradient(180deg,#c9d2de,#5c6f86 45%,#3a3f4a)"></div>
      <div class="panel"><span class="tag">Travel</span><div class="pct">70% Off</div><div class="desc">International Flights<br>Bookings</div><span class="btn-outline">Learn More</span></div>
    </article>
    <article class="offer" style="left:246px">
      <div class="photo" role="img" aria-label="Hotel room with purple curtains" style="background:linear-gradient(90deg,#7a5c8f,#b6a2c4 50%,#6b6e75)"></div>
      <div class="panel"><span class="tag">Hotel</span><div class="pct">60% Off</div><div class="desc">Offering Lowest Hotel<br>Booking Prizes</div><span class="btn-outline">Learn More</span></div>
    </article>
    <article class="offer" style="left:476px">
      <div class="photo" role="img" aria-label="Fashion detail of jeans and leather jacket" style="background:linear-gradient(160deg,#c4b7a6,#3c4b60 55%,#2a3444)"></div>
      <div class="panel"><span class="tag">Fashion</span><div class="pct">50% Off</div><div class="desc">Widest Range Of Designer<br>Cloths</div><span class="btn-outline">Learn More</span></div>
    </article>
    <div class="arrows">
      <svg width="12" height="8" viewBox="0 0 12 8"><path d="M11 4H1M4 1L1 4l3 3" stroke="#222" fill="none"/></svg>
      <svg width="12" height="8" viewBox="0 0 12 8"><path d="M1 4h10M8 1l3 3-3 3" stroke="#fff" fill="none"/></svg>
    </div>
  </div>
  <div class="divider"></div>

  <h2 class="section-title blog-title">Our Latest Blog</h2>

  <!-- featured posts -->
  <article class="card big" style="left:39px">
    <div class="img" role="img" aria-label="Traveller jumping on a desert road below red cliffs" style="background:linear-gradient(180deg,#b9d3ea,#b6855f 45%,#6f6a66)"><div class="ribbon">June 28th, 2016</div><span class="tag">Travel</span></div>
    <h3>The standard Lorem Ipsum passage</h3>
    <p>There are many variations of passages of Lorem Ipsum available, but the majority have suffered alteration in some form, by injected humour, or randomised words which don't look even slightly believable. If you are going to use a passage of Lorem Ipsum, you need to be sure there isn't anything embarrassing hidden in the middle of text...</p>
    <div class="meta">
      <span><svg viewBox="0 0 10 10"><circle cx="5" cy="3" r="2.2" fill="#13416c"/><path d="M1 10c0-3 2-4.5 4-4.5S9 7 9 10z" fill="#13416c"/></svg>Lorem</span>
      <span><svg viewBox="0 0 10 10"><path d="M1 2h8v5H4L2 9V7H1z" fill="none" stroke="#13416c"/></svg>30 Comment</span>
      <span><svg viewBox="0 0 10 10"><path d="M5 9L1.5 5.3A2 2 0 0 1 5 2.6 2 2 0 0 1 8.5 5.3z" fill="none" stroke="#13416c"/></svg>15 Likes</span>
      <span><svg viewBox="0 0 10 10"><circle cx="8" cy="2" r="1.3" fill="#13416c"/><circle cx="2" cy="5" r="1.3" fill="#13416c"/><circle cx="8" cy="8" r="1.3" fill="#13416c"/><path d="M8 2L2 5l6 3" stroke="#13416c" fill="none"/></svg>Share</span>
    </div>
    <div class="more">Continue Reading</div>
  </article>

  <article class="card big" style="left:401px">
    <div class="img" role="img" aria-label="Woman in a hat standing in a greenhouse" style="background:linear-gradient(180deg,#d7dde2,#4f6a4c 45%,#2f3a2f)"><div class="ribbon">June 28th, 2016</div><span class="tag">Fashion</span></div>
    <h3>The standard Lorem Ipsum passage</h3>
    <p>There are many variations of passages of Lorem Ipsum available, but the majority have suffered alteration in some form, by injected humour, or randomised words which don't look even slightly believable. If you are going to use a passage of Lorem Ipsum, you need to be sure there isn't anything embarrassing hidden in the middle of text...</p>
    <div class="meta">
      <span><svg viewBox="0 0 10 10"><circle cx="5" cy="3" r="2.2" fill="#13416c"/><path d="M1 10c0-3 2-4.5 4-4.5S9 7 9 10z" fill="#13416c"/></svg>Lorem</span>
      <span><svg viewBox="0 0 10 10"><path d="M1 2h8v5H4L2 9V7H1z" fill="none" stroke="#13416c"/></svg>35 Comment</span>
      <span><svg viewBox="0 0 10 10"><path d="M5 9L1.5 5.3A2 2 0 0 1 5 2.6 2 2 0 0 1 8.5 5.3z" fill="none" stroke="#13416c"/></svg>30 Likes</span>
      <span><svg viewBox="0 0 10 10"><circle cx="8" cy="2" r="1.3" fill="#13416c"/><circle cx="2" cy="5" r="1.3" fill="#13416c"/><circle cx="8" cy="8" r="1.3" fill="#13416c"/><path d="M8 2L2 5l6 3" stroke="#13416c" fill="none"/></svg>Share</span>
    </div>
    <div class="more">Continue Reading</div>
  </article>

  <!-- row 2 -->
  <aside class="widget" style="left:39px;top:1035px;height:380px">
    <div class="head">Pageloop</div>
    <div class="pl-feed">
      <div class="pl-cover" role="img" aria-label="Page cover photo">
        <div class="av"></div><div class="nm">Solkvartsgillet</div><div class="lk">16,802 likes</div>
        <div class="bt" style="left:6px">Like Page</div><div class="bt" style="left:120px">Share</div>
      </div>
      <div class="line">Be the first of your friends to like this</div>
      <div class="pl-post">
        <div class="who"><i></i>solkvartsgillet.com</div>
        <div class="txt">Det finns sol för alla, se våra nya resor i veckan och dela med vänner</div>
        <div class="pic" role="img" aria-label="Member celebrating outdoors under a blue sky"></div>
      </div>
    </div>
  </aside>

  <article class="card small" style="left:280px;top:1035px">
    <div class="img" role="img" aria-label="Aerial view of a road through autumn forest" style="background:linear-gradient(135deg,#c08a3a,#5d7a3f 50%,#2f4a3a)"><span class="tag">Travel</span></div>
    <div class="date">25 Jun, 2016</div>
    <h3>The standard Lorem Ipsum passage</h3>
    <p>There are many variations of passages of Lorem Ipsum available, but the majority have suffered alteration in some form, by injected humour, or randomised words which don't look even seconn...</p>
    <div class="meta"><span><svg viewBox="0 0 10 10"><circle cx="5" cy="3" r="2.2" fill="#13416c"/><path d="M1 10c0-3 2-4.5 4-4.5S9 7 9 10z" fill="#13416c"/></svg>Lorem</span><span><svg viewBox="0 0 10 10"><path d="M1 2h8v5H4L2 9V7H1z" fill="none" stroke="#13416c"/></svg>30 Comment</span><span><svg viewBox="0 0 10 10"><circle cx="8" cy="2" r="1.3" fill="#13416c"/><circle cx="2" cy="5" r="1.3" fill="#13416c"/><circle cx="8" cy="8" r="1.3" fill="#13416c"/><path d="M8 2L2 5l6 3" stroke="#13416c" fill="none"/></svg>Share</span></div>
    <div class="more">Continue Reading</div>
  </article>

  <article class="card small" style="left:520px;top:1035px">
    <div class="img" role="img" aria-label="Woman in a hat among greenhouse plants" style="background:linear-gradient(180deg,#d5d9dc,#536b4f 50%,#2c352c)"><span class="tag">Lifestyle</span></div>
    <div class="date">26 Jun, 2016</div>
    <h3>The standard Lorem Ipsum passage</h3>
    <p>There are many variations of passages of Lorem Ipsum available, but the majority have suffered alteration in some form, by injected humour, or randomised words which don't look even seconn...</p>
    <div class="meta"><span><svg viewBox="0 0 10 10"><circle cx="5" cy="3" r="2.2" fill="#13416c"/><path d="M1 10c0-3 2-4.5 4-4.5S9 7 9 10z" fill="#13416c"/></svg>Lorem</span><span><svg viewBox="0 0 10 10"><path d="M1 2h8v5H4L2 9V7H1z" fill="none" stroke="#13416c"/></svg>30 Comment</span><span><svg viewBox="0 0 10 10"><circle cx="8" cy="2" r="1.3" fill="#13416c"/><circle cx="2" cy="5" r="1.3" fill="#13416c"/><circle cx="8" cy="8" r="1.3" fill="#13416c"/><path d="M8 2L2 5l6 3" stroke="#13416c" fill="none"/></svg>Share</span></div>
    <div class="more">Continue Reading</div>
  </article>

  <!-- row 3 -->
  <article class="card small" style="left:39px;top:1473px">
    <div class="img" role="img" aria-label="Blonde woman in a hat outdoors" style="background:linear-gradient(180deg,#5a6a3e,#b89a6a 55%,#6b5840)"><span class="tag">Calories</span></div>
    <div class="date">22 Aug, 2016</div>
    <h3>The standard Lorem Ipsum passage</h3>
    <p>There are many variations of passages of Lorem Ipsum available, but the majority have suffered alteration in some form, by injected humour, or randomised words which don't look even seconn...</p>
    <div class="meta"><span><svg viewBox="0 0 10 10"><circle cx="5" cy="3" r="2.2" fill="#13416c"/><path d="M1 10c0-3 2-4.5 4-4.5S9 7 9 10z" fill="#13416c"/></svg>Lorem</span><span><svg viewBox="0 0 10 10"><path d="M1 2h8v5H4L2 9V7H1z" fill="none" stroke="#13416c"/></svg>30 Comment</span><span><svg viewBox="0 0 10 10"><circle cx="8" cy="2" r="1.3" fill="#13416c"/><circle cx="2" cy="5" r="1.3" fill="#13416c"/><circle cx="8" cy="8" r="1.3" fill="#13416c"/><path d="M8 2L2 5l6 3" stroke="#13416c" fill="none"/></svg>Share</span></div>
    <div class="more">Continue Reading</div>
  </article>

  <article class="card small" style="left:280px;top:1473px">
    <div class="img" role="img" aria-label="Fashion detail of jeans and jacket" style="background:linear-gradient(160deg,#b3a79a,#3f4c5d 55%,#2b323c)"><span class="tag">Fashion</span></div>
    <div class="date">26 Aug, 2016</div>
    <h3>The standard Lorem Ipsum passage</h3>
    <p>There are many variations of passages of Lorem Ipsum available, but the majority have suffered alteration in some form, by injected humour, or randomised words which don't look even seconn...</p>
    <div class="meta"><span><svg viewBox="0 0 10 10"><circle cx="5" cy="3" r="2.2" fill="#13416c"/><path d="M1 10c0-3 2-4.5 4-4.5S9 7 9 10z" fill="#13416c"/></svg>Lorem</span><span><svg viewBox="0 0 10 10"><path d="M1 2h8v5H4L2 9V7H1z" fill="none" stroke="#13416c"/></svg>30 Comment</span><span><svg viewBox="0 0 10 10"><circle cx="8" cy="2" r="1.3" fill="#13416c"/><circle cx="2" cy="5" r="1.3" fill="#13416c"/><circle cx="8" cy="8" r="1.3" fill="#13416c"/><path d="M8 2L2 5l6 3" stroke="#13416c" fill="none"/></svg>Share</span></div>
    <div class="more">Continue Reading</div>
  </article>

  <aside class="widget" style="left:520px;top:1473px;height:416px">
    <div class="head">Glimtora</div>
    <div class="ig-handle">@solkvartsgillet</div>
    <div class="ig-stats"><span><i></i>200 Photos</span><span><i></i>140 Followers</span></div>
    <div class="ig-grid">
      <div role="img" aria-label="Feed photo" style="background:#4d5d45"></div>
      <div role="img" aria-label="Feed photo" style="background:#8a7a6a"></div>
      <div role="img" aria-label="Feed photo" style="background:#a9a39a"></div>
      <div role="img" aria-label="Feed photo" style="background:#6a5a4a"></div>
      <div role="img" aria-label="Feed photo" style="background:#b08f5e"></div>
      <div role="img" aria-label="Feed photo" style="background:#5e6a74"></div>
      <div role="img" aria-label="Feed photo" style="background:#7b7f5c"></div>
      <div role="img" aria-label="Feed photo" style="background:#3f3a38"></div>
      <div role="img" aria-label="Feed photo" style="background:#9a7d72"></div>
      <div role="img" aria-label="Feed photo" style="background:#564a44"></div>
      <div role="img" aria-label="Feed photo" style="background:#8c8f95"></div>
      <div role="img" aria-label="Feed photo" style="background:#6e5340"></div>
    </div>
    <div class="ig-foot">Powered by Solkvartsgillet</div>
  </aside>

  <!-- row 4 -->
  <article class="card small" style="left:39px;top:1910px">
    <div class="img" role="img" aria-label="Suspension bridge across an autumn valley" style="background:linear-gradient(180deg,#c7d5e4,#a9763f 50%,#4d4030)"><span class="tag">Travel</span></div>
    <div class="date">22 Sept, 2016</div>
    <h3>The standard Lorem Ipsum passage</h3>
    <p>There are many variations of passages of Lorem Ipsum available, but the majority have suffered alteration in some form, by injected humour, or randomised words which don't look even seconn...</p>
    <div class="meta"><span><svg viewBox="0 0 10 10"><circle cx="5" cy="3" r="2.2" fill="#13416c"/><path d="M1 10c0-3 2-4.5 4-4.5S9 7 9 10z" fill="#13416c"/></svg>Lorem</span><span><svg viewBox="0 0 10 10"><path d="M1 2h8v5H4L2 9V7H1z" fill="none" stroke="#13416c"/></svg>30 Comment</span><span><svg viewBox="0 0 10 10"><circle cx="8" cy="2" r="1.3" fill="#13416c"/><circle cx="2" cy="5" r="1.3" fill="#13416c"/><circle cx="8" cy="8" r="1.3" fill="#13416c"/><path d="M8 2L2 5l6 3" stroke="#13416c" fill="none"/></svg>Share</span></div>
    <div class="more">Continue Reading</div>
  </article>

  <article class="card small" style="left:280px;top:1910px">
    <div class="img" role="img" aria-label="Woman in a wheat field at golden hour" style="background:linear-gradient(180deg,#9fc4e0,#d9c08a 55%,#b3893f)"><span class="tag">Lifestyle</span></div>
    <div class="date">26 Sept, 2016</div>
    <h3>The standard Lorem Ipsum passage</h3>
    <p>There are many variations of passages of Lorem Ipsum available, but the majority have suffered alteration in some form, by injected humour, or randomised words which don't look even seconn...</p>
    <div class="meta"><span><svg viewBox="0 0 10 10"><circle cx="5" cy="3" r="2.2" fill="#13416c"/><path d="M1 10c0-3 2-4.5 4-4.5S9 7 9 10z" fill="#13416c"/></svg>Lorem</span><span><svg viewBox="0 0 10 10"><path d="M1 2h8v5H4L2 9V7H1z" fill="none" stroke="#13416c"/></svg>30 Comment</span><span><svg viewBox="0 0 10 10"><circle cx="8" cy="2" r="1.3" fill="#13416c"/><circle cx="2" cy="5" r="1.3" fill="#13416c"/><circle cx="8" cy="8" r="1.3" fill="#13416c"/><path d="M8 2L2 5l6 3" stroke="#13416c" fill="none"/></svg>Share</span></div>
    <div class="more">Continue Reading</div>
  </article>

  <article class="card small" style="left:520px;top:1910px">
    <div class="img" role="img" aria-label="Woman crossing a city street" style="background:linear-gradient(180deg,#cfd3d6,#8c8e90 55%,#4a4c4f)"><span class="tag">Fashion</span></div>
    <div class="date">26 Aug, 2016</div>
    <h3>The standard Lorem Ipsum passage</h3>
    <p>There are many variations of passages of Lorem Ipsum available, but the majority have suffered alteration in some form, by injected humour, or randomised words which don't look even seconn...</p>
    <div class="meta"><span><svg viewBox="0 0 10 10"><circle cx="5" cy="3" r="2.2" fill="#13416c"/><path d="M1 10c0-3 2-4.5 4-4.5S9 7 9 10z" fill="#13416c"/></svg>Lorem</span><span><svg viewBox="0 0 10 10"><path d="M1 2h8v5H4L2 9V7H1z" fill="none" stroke="#13416c"/></svg>30 Comment</span><span><svg viewBox="0 0 10 10"><circle cx="8" cy="2" r="1.3" fill="#13416c"/><circle cx="2" cy="5" r="1.3" fill="#13416c"/><circle cx="8" cy="8" r="1.3" fill="#13416c"/><path d="M8 2L2 5l6 3" stroke="#13416c" fill="none"/></svg>Share</span></div>
    <div class="more">Continue Reading</div>
  </article>

  <div class="load-more">LOAD MORE</div>
</main>

<footer class="abs foot-gold">
  <div class="mark"></div>
  <div class="name">Solkvartsgillet</div>
  <p>There are many variations of passages of Lorem Ipsum available, majority have suffered alteration in some form, by injected humour, or randomised words which don't look even slightly believable.</p>
  <div class="sub">Email Subscription</div>
  <form><div class="input">Enter Your Email...</div><div class="send"><svg width="10" height="10" viewBox="0 0 10 10"><path d="M1 5l8-4-3 8-1.5-3z" fill="#fff"/></svg></div></form>
</footer>

<div class="abs foot-dark">
  <div class="icons"><span></span><span class="on"></span><span></span><span></span><span></span><span></span></div>
  <div class="copy">Copyright © 2016 Solkvartsgillet</div>
</div>

</body>
</html>
```